Eye-Catching, Direct Marketing Residential Painting Flyer!

I am run a residential painting business and am looking for a flyer to be designed to mailout to potential customers.
I want the copy/wording to be designed similar to this flyer.

It's important that the person reading the flyer gets the benefits we're promoting which is why I want the wording/copy to be almost identical to the flyer attached.

However, the structure will be different. The flyer will be a postcard thick, 5 x11.5.
Double sided.

The name of the company is Brightwall Coaters.

I would also like the prominent colour to either be light green or orange.

Target Market(s)

Home Owners between the age of 45-80.

Industry/Entity Type

Painting And Decorating

Font styles to use
Serif

Colors
f68d4d
faa54b
f78f20
f37122
9bcb3c
abd037
cadf82

Requirements
Must have
• Excellent Eye-Catching Design
• Benefits Visibly Promoted
• Action Taking Incentive- Call Now for FREE Window Cleaning and FREE Painting Estimate
Should not have
• Crowded wording

```html
<!DOCTYPE html>
<html lang="en">
<head>
<meta charset="utf-8">
<title>Brightwall Coaters – Painting Flyer</title>
<link rel="stylesheet" href="https://fonts.googleapis.com/css2?family=Kalam:wght@300;400&family=Source+Sans+3:ital,wght@0,600;1,600&family=Rubik+Dirt&display=swap">
<style>
  :root {
    --wood-light: #9cb987;
    --wood-mid: #88a775;
    --wood-dark: #6f8c60;
    --panel: #d6e6a0;
    --orange: #f37122;
    --orange-bright: #f78f20;
    --orange-soft: #faa54b;
    --note: #f8ef8c;
    --white: #ffffff;
  }
  * { box-sizing: border-box; margin: 0; padding: 0; }
  html, body { width: 1200px; height: 522px; overflow: hidden; background: #ffffff; }
  .flyer { position: relative; width: 1200px; height: 522px; overflow: hidden; }

  .wood-backdrop {
    position: absolute; inset: 0;
    background:
      linear-gradient(180deg, var(--wood-light) 0%, var(--wood-mid) 45%, var(--wood-light) 70%, var(--wood-dark) 100%);
  }

  .question-panel {
    position: absolute; left: 53px; top: 42px; width: 869px; height: 334px;
    background: var(--panel); border-radius: 13px;
    box-shadow: 0 3px 8px rgba(0,0,0,0.25);
  }
  .script {
    position: absolute; font-family: "Kalam", cursive; font-weight: 300;
    color: var(--orange); font-size: 36px; line-height: 1;
  }
  .script--does { left: 40px; top: 36px; }
  .script--look { left: 40px; top: 155px; }

  .surface-list {
    position: absolute; left: 53px; top: 73px; width: 500px;
    display: grid; grid-template-columns: 210px 208px 180px; row-gap: 13px;
    list-style: none;
    font-family: "Source Sans 3", sans-serif; font-weight: 600;
    font-size: 25px; color: var(--orange); line-height: 26px;
  }
  .surface-list li { display: flex; align-items: center; gap: 15px; white-space: nowrap; }
  .checkbox { width: 26px; height: 26px; border: 2px solid var(--orange); flex: none; }

  .headline {
    position: absolute; left: 51px; top: 193px;
    font-family: "Rubik Dirt", sans-serif; font-weight: 400;
    font-size: 45px; line-height: 56px; color: var(--orange);
    letter-spacing: 1px; white-space: nowrap; text-transform: uppercase;
  }

  .rot-band { position: absolute; left: 30px; top: 392px; width: 800px; height: 58px; }
  .rot-band__text {
    position: absolute; left: 146px; top: 394px; height: 56px;
    display: flex; align-items: center;
    font-family: "Source Sans 3", sans-serif; font-style: italic; font-weight: 600;
    font-size: 27px; color: var(--white); white-space: nowrap;
  }

  .sticky-note {
    position: absolute; left: 905px; top: 205px; width: 236px; height: 236px;
    background: var(--note); transform: rotate(-13deg);
    box-shadow: 2px 5px 10px rgba(0,0,0,0.3);
  }
  .sticky-note__ring { position: absolute; inset: 20px 14px; }
  .sticky-note__text {
    position: absolute; left: 30px; top: 58px; width: 180px;
    transform: rotate(-16deg); text-align: center;
    font-family: "Kalam", cursive; font-weight: 400; font-size: 22px; line-height: 1.35;
    color: var(--orange-bright);
  }
</style>
</head>
<body>
<main class="flyer">
  <div class="wood-backdrop" role="img" aria-label="Weathered green painted wooden boards with peeling paint"></div>

  <section class="question-panel">
    <p class="script script--does">Does your</p>
    <ul class="surface-list">
      <li><span class="checkbox"></span>Deck</li>
      <li><span class="checkbox"></span>Interior</li>
      <li><span class="checkbox"></span>Sliding</li>
      <li><span class="checkbox"></span>Walls</li>
      <li><span class="checkbox"></span>Fence</li>
      <li><span class="checkbox"></span>Windows</li>
    </ul>
    <p class="script script--look">Look</p>
    <h1 class="headline">Faded, dirty, out-of-date,<br>chipped, or peeling?</h1>
  </section>

  <svg class="rot-band" viewBox="0 0 800 58" preserveAspectRatio="none" aria-hidden="true">
    <path fill="#f37122" d="M14 4 L786 2 L778 10 L796 16 L784 24 L800 32 L786 40 L794 48 L780 56 L20 58 L26 50 L6 44 L18 36 L0 28 L16 20 L4 12 Z"/>
  </svg>
  <p class="rot-band__text">Has the wood started to rot yet?</p>

  <aside class="sticky-note">
    <svg class="sticky-note__ring" viewBox="0 0 208 196" aria-hidden="true">
      <path d="M40 40 C80 5 170 5 195 60 C215 120 170 185 100 188 C40 190 5 150 10 105 C14 70 30 55 48 48"
            fill="none" stroke="#faa54b" stroke-width="2.5" stroke-linecap="round"/>
    </svg>
    <p class="sticky-note__text">Take control of how your home looks!</p>
  </aside>
</main>
</body>
</html>
```